CrestHornSupply.com

I need a new webdesign for a company in the San Jose/SF Bay area that showcases the financial benefits of buying used band instruments for junior high students.This would be opposed to the current and costly option of renting cheap quality instruments from the 2 or 3 local music stores that charge a monthly fee that over the years charges the buyer 3 or 4x over..
Instruments: focus in on Alto Sax, Trumpet, Flute, Clarinet, Trombone, Tenor Sax, Baritone
Target middle schools are Willowmere Middle School and Harlan Middle School in San Jose, CA. Both have award winning band programs.
Files attached may or may not be important.
Tabs Needed and funtional
Contact
Shopping Cart
Select Instrument
Checkout
Add to Cart, etc.
Instuments
quantity, etc.
trade in your instrument/sell your instrument
ability to add or take away new instruments for sale. including pictures
Additional questions or info, feel free to ask
Updates
Hi Designers,
Project Deadline Extended
Reason: In the next week you will be receiving specific content that will be required to be had on the website.
New desigins are still welcome. Please continue to contact me if you have questions about your individual designs.
Thanks!
Crest Horn

```html
<!DOCTYPE html>
<html lang="en">
<head>
<meta charset="utf-8">
<title>Crest Horn Instruments</title>
<link href="https://fonts.googleapis.com/css2?family=Open+Sans:wght@400;600;700&display=swap" rel="stylesheet">
<style>
:root{
  --red:#a51417;
  --red-dark:#8e0d10;
  --red-soft:#c0262b;
  --panel:#ffffff;
  --card:#eeeeee;
  --ink:#3a3a3a;
  --muted:#555555;
  --bar:#7d0c0e;
  --brass:#c9a23a;
  --brass-deep:#8a6a1c;
  --wood:#2a2d33;
  --sax-blue:#3b4a7a;
}
*{margin:0;padding:0;box-sizing:border-box}
html,body{width:974px;height:1200px;overflow:hidden}
body{position:relative;background:linear-gradient(180deg,#b5252a 0%,#a81418 35%,#a10f12 100%);font-family:"Open Sans",Arial,sans-serif;color:var(--ink)}
.abs{position:absolute}
.backdrop-photo{left:0;top:0;width:974px;height:430px;
  background:
    radial-gradient(ellipse 90px 140px at 60px 260px,rgba(255,255,255,.10),rgba(255,255,255,0)),
    radial-gradient(ellipse 90px 140px at 915px 260px,rgba(255,255,255,.10),rgba(255,255,255,0)),
    radial-gradient(ellipse 70px 50px at 110px 90px,rgba(255,255,255,.16),rgba(255,255,255,0)),
    radial-gradient(ellipse 70px 50px at 880px 90px,rgba(255,255,255,.16),rgba(255,255,255,0)),
    linear-gradient(180deg,rgba(255,255,255,.14),rgba(255,255,255,0))}
.logo-mark{left:139px;top:18px;width:54px;height:54px;border-radius:50%;background:#f4f4f4}
.logo-name{left:201px;top:20px;color:#fff;font-weight:700;font-size:20px;line-height:24px;letter-spacing:1.5px}
.top-tools{left:594px;top:0;height:28px;display:flex}
.top-tools span{width:30px;height:28px;background:var(--bar);border-right:1px solid #6a0a0c;display:flex;align-items:center;justify-content:center}
.top-tools span.on{background:#1c1c1c}
.top-tools .cart{width:90px;color:#fff;font-size:8px;font-weight:600;gap:4px}
.phone{left:706px;top:48px;color:#fff;font-weight:700;font-size:15px;display:flex;align-items:center;gap:5px}
.nav{left:139px;top:88px;width:695px;height:38px;background:#fff;border-bottom:2px solid var(--red)}
.nav .home{position:absolute;left:1px;top:0;width:47px;height:38px;background:var(--red-dark);display:flex;align-items:center;justify-content:center}
.nav a{position:absolute;top:12px;transform:translateX(-50%);color:var(--red);font-size:10.5px;text-decoration:none}
.sheet{left:139px;top:126px;width:695px;height:1023px;background:var(--panel)}
.slider{left:144px;top:131px;width:686px;height:239px;overflow:hidden;
  background:
    radial-gradient(ellipse 18px 24px at 160px 42px,rgba(255,255,255,.85),rgba(255,255,255,0)),
    radial-gradient(ellipse 18px 24px at 295px 30px,rgba(255,255,255,.85),rgba(255,255,255,0)),
    radial-gradient(ellipse 18px 24px at 435px 28px,rgba(255,255,255,.85),rgba(255,255,255,0)),
    radial-gradient(ellipse 18px 24px at 555px 34px,rgba(255,255,255,.85),rgba(255,255,255,0)),
    radial-gradient(ellipse 18px 24px at 640px 46px,rgba(255,255,255,.85),rgba(255,255,255,0)),
    linear-gradient(90deg,rgba(0,0,0,0) 0%,rgba(255,255,255,.18) 14%,rgba(0,0,0,0) 22%,rgba(255,255,255,.18) 36%,rgba(0,0,0,0) 44%,rgba(255,255,255,.18) 58%,rgba(0,0,0,0) 66%,rgba(255,255,255,.18) 80%,rgba(0,0,0,0) 90%),
    linear-gradient(180deg,#bdb8b4 0%,#b9a9a6 14%,#b8252a 30%,#c8343a 52%,#9c1c20 72%,#3a3a3e 86%,#6e6e72 100%)}
.slider-caption{left:144px;top:302px;width:686px;height:43px;background:linear-gradient(90deg,rgba(0,0,0,0) 18%,rgba(0,0,0,.5) 32%,rgba(0,0,0,.5) 68%,rgba(0,0,0,0) 82%);color:#fff;font-weight:700;font-size:15px;letter-spacing:1.5px;text-align:center;line-height:43px}
.arrow{top:243px;width:28px;height:24px;display:flex;align-items:center;justify-content:center}
.dots{left:449px;top:354px;display:flex;gap:3px}
.dots i{width:8px;height:8px;border-radius:50%;background:#fff;display:block}
.dots i.on{background:var(--red);box-shadow:0 0 0 1.5px #fff inset}
h2{position:absolute;color:var(--red);font-weight:600;font-size:19.5px;line-height:24px}
.intro{left:155px;top:439px;width:434px;font-family:Arial,sans-serif;font-size:7.2px;line-height:9px;color:var(--muted)}
.intro p{margin-bottom:8px}
.card{position:absolute;width:132px;height:138px;background:var(--card)}
.card .pic{position:absolute;left:14px;top:8px;width:104px;height:100px}
.pic.clarinet{background:
  linear-gradient(100deg,rgba(238,238,238,0) 18%,rgba(42,45,51,.55) 22%,rgba(238,238,238,0) 26%,rgba(238,238,238,0) 36%,rgba(42,45,51,.55) 40%,rgba(238,238,238,0) 44%,rgba(238,238,238,0) 54%,rgba(42,45,51,.55) 58%,rgba(238,238,238,0) 62%,rgba(238,238,238,0) 72%,rgba(42,45,51,.55) 76%,rgba(238,238,238,0) 80%),
  radial-gradient(ellipse 50% 48% at 50% 48%,rgba(42,45,51,.22),rgba(238,238,238,0))}
.pic.brass{background:
  linear-gradient(150deg,rgba(238,238,238,0) 30%,rgba(201,162,58,.75) 46%,rgba(138,106,28,.6) 54%,rgba(238,238,238,0) 70%),
  radial-gradient(ellipse 45% 40% at 30% 30%,rgba(201,162,58,.35),rgba(238,238,238,0))}
.pic.trumpet{background:
  linear-gradient(165deg,rgba(238,238,238,0) 38%,rgba(201,162,58,.8) 48%,rgba(138,106,28,.65) 56%,rgba(238,238,238,0) 66%),
  radial-gradient(ellipse 28% 30% at 85% 40%,rgba(201,162,58,.55),rgba(238,238,238,0))}
.pic.sax{background:
  linear-gradient(75deg,rgba(238,238,238,0) 36%,rgba(59,74,122,.7) 46%,rgba(201,162,58,.7) 54%,rgba(238,238,238,0) 64%),
  radial-gradient(ellipse 30% 24% at 62% 78%,rgba(59,74,122,.55),rgba(238,238,238,0))}
.pic.flute{background:
  linear-gradient(125deg,rgba(165,20,23,0) 22%,rgba(40,20,22,.75) 30%,rgba(70,20,22,.7) 70%,rgba(165,20,23,0) 78%)}
.card .name{position:absolute;left:0;width:132px;bottom:6px;text-align:center;font-size:13px;color:#444}
.card.featured{background:var(--red);height:168px}
.card.featured .name{bottom:auto;top:74px;color:#fff;font-weight:600;font-size:12px}
.card.featured .price{position:absolute;top:92px;width:132px;text-align:center;color:#fff;font-size:6.5px}
.card.featured .acts{position:absolute;left:25px;top:136px;display:flex;gap:3px}
.acts span{width:26px;height:20px;background:#d4d4d4;display:flex;align-items:center;justify-content:center}
.acts span.hot{background:var(--red-dark)}
.side{position:absolute;left:608px;width:221px;background:var(--card)}
.side h3{color:var(--red);font-weight:600;font-size:19px;line-height:22px;padding:8px 0 0 8px}
.news-item{position:relative;height:50px}
.news-item.on{background:var(--red-dark)}
.news-item .thumb{position:absolute;left:8px;top:5px;width:60px;height:40px;background:linear-gradient(180deg,#c9b9b0 0%,#b3403a 50%,#7a2420 100%)}
.news-item .t{position:absolute;left:73px;top:6px;font-family:Arial,sans-serif;font-size:7.2px;font-weight:700;color:#333}
.news-item .d{position:absolute;left:73px;top:21px;width:142px;font-family:Arial,sans-serif;font-size:7px;line-height:9px;color:#444}
.news-item.on .t,.news-item.on .d{color:#fff}
.feature .thumb{position:absolute;left:8px;width:60px;height:40px;background:var(--red-soft);display:flex;align-items:center;justify-content:center}
.feature .d{position:absolute;left:73px;width:142px;font-family:Arial,sans-serif;font-size:7px;line-height:9.2px;color:#555}
.social{top:1162px;width:22px;height:22px;border-radius:50%;background:#2c6fb8}
.copy{right:146px;top:1167px;font-family:Arial,sans-serif;font-size:8px;color:#fff}
</style>
</head>
<body>
<div class="abs backdrop-photo" role="img" aria-label="Faded photo of a marching band in red uniforms"></div>

<div class="abs logo-mark"></div>
<div class="abs logo-name">CREST HORN<br>INSTRUMENTS</div>

<div class="abs top-tools">
  <span><svg width="10" height="9" viewBox="0 0 10 9"><path d="M5 9 1 5A2.3 2.3 0 0 1 5 1.6 2.3 2.3 0 0 1 9 5Z" fill="#ddd"/></svg></span>
  <span><svg width="9" height="10" viewBox="0 0 9 10"><circle cx="4.5" cy="3" r="2.3" fill="#ddd"/><path d="M0 10a4.5 4 0 0 1 9 0Z" fill="#ddd"/></svg></span>
  <span><svg width="10" height="10" viewBox="0 0 10 10"><rect x="1" y="2" width="7" height="7" fill="none" stroke="#ddd"/><path d="M4 6 9 1" stroke="#ddd"/></svg></span>
  <span><svg width="8" height="10" viewBox="0 0 8 10"><rect x="1" y="4" width="6" height="6" fill="#ddd"/><path d="M2 4V2.5a2 2 0 0 1 4 0V4" fill="none" stroke="#ddd"/></svg></span>
  <span class="on"><svg width="10" height="10" viewBox="0 0 10 10"><circle cx="2" cy="5" r="1.6" fill="#fff"/><circle cx="8" cy="2" r="1.6" fill="#fff"/><circle cx="8" cy="8" r="1.6" fill="#fff"/><path d="M2 5 8 2M2 5l6 3" stroke="#fff"/></svg></span>
  <span class="cart"><svg width="12" height="10" viewBox="0 0 12 10"><path d="M0 1h2l2 6h6l1.5-4.5H3" fill="none" stroke="#fff"/><circle cx="5" cy="9" r="1" fill="#fff"/><circle cx="9" cy="9" r="1" fill="#fff"/></svg>Cart: (empty)</span>
</div>

<div class="abs phone"><svg width="13" height="13" viewBox="0 0 13 13"><path d="M3 1 5 4 3.6 5.4a7 7 0 0 0 4 4L9 8l3 2-1.5 2C5 12 1 7 1 2.5Z" fill="#fff"/></svg>10 20 30 40 50</div>

<nav class="abs nav">
  <div class="home"><svg width="13" height="11" viewBox="0 0 13 11"><path d="M6.5 0 13 5.5h-2V11H8V7.5H5V11H2V5.5H0Z" fill="#fff"/></svg></div>
  <a style="left:139px">INSTRUMENTS</a>
  <a style="left:264px">TRADE IN</a>
  <a style="left:376px">SELL OUT</a>
  <a style="left:478px">LOGIN</a>
  <a style="left:580px">CONTACT</a>
</nav>

<div class="abs sheet"></div>

<div class="abs slider" role="img" aria-label="Photo of a school marching band drumline in red and white uniforms with tall white plumes"></div>
<div class="abs slider-caption">WILLOWMERE MIDDLE SCHOOL</div>
<div class="abs arrow" style="left:148px;background:rgba(140,140,140,.5)"><svg width="10" height="8" viewBox="0 0 10 8"><path d="M10 4H2M5 1 2 4l3 3" stroke="#fff" stroke-width="1.6" fill="none"/></svg></div>
<div class="abs arrow" style="left:795px;background:#f2f2f2"><svg width="10" height="8" viewBox="0 0 10 8"><path d="M0 4h8M5 1l3 3-3 3" stroke="#a51417" stroke-width="1.6" fill="none"/></svg></div>
<div class="abs dots"><i></i><i></i><i class="on"></i><i></i><i></i><i></i><i></i></div>

<h2 style="left:155px;top:401px">Welcome To Crest Horn Instruments</h2>
<div class="abs intro">
  <p>We show you financial benefits of buying used band instruments for junior high students.This would be opposed to the current and costly option of renting cheap quality instruments from the 2 or 3 local music stores that charge a monthly fee that over the years charges the buyer 3 or 4x over..</p>
  <p>Ut wisi enim ad minim veniam, quis nostrud exerci tation ullamcorper suscipit lobortis nisl ut aliquip ex ea commodo consequat. Duis autem vel eum iriure dolor in hendrerit in vulputate velit esse molestie consequat, vel illum dolore eu feugiat nulla facilisis at vero eros et accumsan et iusto odio dignissim qui blandit praesent luptatum zzril delenit augue duis dolore te feugait nulla facilisi.</p>
  <p>Scipit lobortis nisl ut aliquip ex ea commodo consequat. Duis autem vel eum iriure dolor in hendrerit in vulputate velit esse molestie consequat, vel illum dolore eu feugiat nulla facilisis at vero eros et accumsan et iusto odio dignissim qui blandit praesent luptatum zzril delenit augue duis dolore te feugait nulla facilisi.</p>
</div>

<h2 style="left:155px;top:556px">Latest Products</h2>

<div class="card featured" style="left:155px;top:590px">
  <div class="pic flute" role="img" aria-label="Photo of a flute"></div>
  <svg class="abs" style="left:57px;top:52px" width="18" height="18" viewBox="0 0 18 18"><circle cx="7.5" cy="7.5" r="5.5" fill="none" stroke="#fff" stroke-width="2"/><path d="M11.5 11.5 16 16M5 7.5h5M7.5 5v5" stroke="#fff" stroke-width="2"/></svg>
  <div class="name">FLUTE</div>
  <div class="price">$50.00</div>
  <div class="acts">
    <span><svg width="10" height="8" viewBox="0 0 12 10"><path d="M0 1h2l2 6h6l1.5-4.5H3" fill="none" stroke="#aaa"/></svg></span>
    <span><svg width="11" height="7" viewBox="0 0 11 7"><ellipse cx="5.5" cy="3.5" rx="5" ry="3" fill="none" stroke="#aaa"/><circle cx="5.5" cy="3.5" r="1.3" fill="#aaa"/></svg></span>
    <span class="hot"><svg width="11" height="11" viewBox="0 0 11 11"><path d="M5.5.5 7 4h3.5L7.7 6.2 8.8 10 5.5 7.8 2.2 10l1.1-3.8L.5 4H4Z" fill="none" stroke="#fff"/></svg></span>
  </div>
</div>
<div class="card" style="left:308px;top:590px"><div class="pic clarinet" role="img" aria-label="Photo of clarinets"></div><div class="name">Clarinet</div></div>
<div class="card" style="left:461px;top:590px"><div class="pic brass" role="img" aria-label="Photo of a trombone"></div><div class="name">Trombone</div></div>

<div class="card" style="left:155px;top:774px"><div class="pic sax" role="img" aria-label="Photo of an alto saxophone"></div><div class="name">Alto Sax</div></div>
<div class="card" style="left:308px;top:774px"><div class="pic trumpet" role="img" aria-label="Photo of a trumpet"></div><div class="name">Trumpet</div></div>
<div class="card" style="left:461px;top:774px"><div class="pic clarinet" role="img" aria-label="Photo of clarinets"></div><div class="name">Clarinet</div></div>

<div class="card" style="left:155px;top:952px"><div class="pic sax" role="img" aria-label="Photo of an alto saxophone"></div><div class="name">Alto Sax</div></div>
<div class="card" style="left:308px;top:952px"><div class="pic trumpet" role="img" aria-label="Photo of a trumpet"></div><div class="name">Trumpet</div></div>
<div class="card" style="left:461px;top:952px"><div class="pic clarinet" role="img" aria-label="Photo of clarinets"></div><div class="name">Clarinet</div></div>

<aside class="side" style="top:386px;height:152px">
  <h3>Latest News</h3>
  <div class="news-item on" style="margin-top:6px">
    <div class="thumb" role="img" aria-label="Photo of a marching band performance"></div>
    <div class="t">Lorem Ipsum Dolor</div>
    <div class="d">Ut wisi enim ad minim veniam, quis nostrud exerci tation ullamcorper ....</div>
  </div>
  <div class="news-item">
    <div class="thumb" role="img" aria-label="Photo of a marching band performance"></div>
    <div class="t">Lorem Ipsum Dolor</div>
    <div class="d">Ut wisi enim ad minim veniam, quis nostrud exerci tation ullamcorper ....</div>
  </div>
</aside>

<aside class="side feature" style="top:542px;height:132px">
  <h3>Rent-to-Own<br>Musical Instruments</h3>
  <div class="thumb" style="top:72px"><svg width="11" height="11" viewBox="0 0 18 18"><circle cx="7.5" cy="7.5" r="5.5" fill="none" stroke="#fff" stroke-width="2.4"/><path d="M11.5 11.5 16 16" stroke="#fff" stroke-width="2.4"/></svg></div>
  <div class="d" style="top:71px">Rent to own your own musical instrument in the San Jose area! All rental payments apply to the purchase.<br><br>Check Rent to Own for more info!</div>
</aside>

<aside class="side feature" style="top:679px;height:152px">
  <h3>Music Lessons in San<br>Jose</h3>
  <div class="thumb" style="top:69px"><svg width="11" height="11" viewBox="0 0 18 18"><circle cx="7.5" cy="7.5" r="5.5" fill="none" stroke="#fff" stroke-width="2.4"/><path d="M11.5 11.5 16 16" stroke="#fff" stroke-width="2.4"/></svg></div>
  <div class="d" style="top:69px">We have music lessons for students of all ages. Tune Hall offers music lessons for all the major instruments like clarinet, trumpet, saxophone, flute violin, piano, guitar, bass, voice, and drums. Come learn an instrument with our experienced music teachers!</div>
</aside>

<aside class="side feature" style="top:836px;height:153px">
  <h3>Musical Instrument<br>Repairs</h3>
  <div class="thumb" style="top:67px"><svg width="11" height="11" viewBox="0 0 18 18"><circle cx="7.5" cy="7.5" r="5.5" fill="none" stroke="#fff" stroke-width="2.4"/><path d="M11.5 11.5 16 16" stroke="#fff" stroke-width="2.4"/></svg></div>
  <div class="d" style="top:66px">Highly experienced musical instrument repair professionals will repair your string, woodwind and brass instruments. In house repairs, walk-ins welcome. Our staff will also remove dents, tune and restring instruments.</div>
</aside>

<aside class="side feature" style="top:994px;height:138px">
  <h3>Music Teacher<br>Profile</h3>
  <div class="thumb" style="top:67px"><svg width="11" height="11" viewBox="0 0 18 18"><circle cx="7.5" cy="7.5" r="5.5" fill="none" stroke="#fff" stroke-width="2.4"/><path d="M11.5 11.5 16 16" stroke="#fff" stroke-width="2.4"/></svg></div>
  <div class="d" style="top:66px">Highly experienced music teacher professionals will teach you string, woodwind and brass instruments. In house repairs, walk-ins welcome. Our staff will also remove dents, tune and restring instruments.</div>
</aside>

<div class="abs social" style="left:149px"></div>
<div class="abs social" style="left:176px;background:#2d9ad6"></div>
<div class="abs social" style="left:203px"></div>
<div class="abs social" style="left:230px;background:#e56b8b"></div>
<div class="abs copy">Copyright © 2014 CREST HORN INSTRUMENTS. All Rights Reserved.</div>
</body>
</html>
```